Cover Design Brief – Prayer Book (Modern Revision)

Design a new, modern, high-quality book cover that reflects the essence of the original version. The updated cover should feel contemporary yet familiar, appealing to both younger and older readers, while evoking a sense of spiritual depth, calm, and authenticity.

1. Visual Reference to the Original Cover
Continuity:
Retain visual elements such as the color palette, central motifs (eg, geometric patterns, Islamic ornaments, or a symbolic figure), and overall structure from the original cover.

Recognition:
Readers familiar with the old cover should instantly recognize the book but be pleasantly surprised by the refined, modern look.

2. Style & Mood
Modern Islamic design, minimalist and clean rather than ornate.

Spiritual, calming, elegant – avoid overly bright or flashy visuals.

Subtle use of Islamic motifs, possibly a decorative Arabic calligraphy word like ṣalāh (صلاة) to enrich the theme.

3. Suggested Color Palette
Deep blue, teal, petrol green, olive, sand tones, or midnight blue with accents of gold – depending on the original cover scheme.

Avoid neon or loud colors.

If gold or silver is used, it should be subtle and classy (eg, foil stamping or embossing, not digital effects).

4. Typography
A modern serif font for the main title is welcome, but it should be clean and elegant.

Subtitles should use a clear, legible font.

If the title includes Arabic text, it should be displayed in tasteful classical calligraphy or a stylized script.

5. Back Cover
Will include a brief description text (to be provided later).

Clean layout, optionally with a small publisher logo.

Possibly a short quote or ḥadīth in Arabic (with or without translation) to complement the design.

6. Target Audience
German-speaking Muslims, male and female, ages 15+

Suitable for both beginners and advanced practitioners of the prayer

Designed as a long-term spiritual companion and a thoughtful gift

```html
<!DOCTYPE html>
<html lang="de">
<head>
<meta charset="utf-8">
<title>Ṣalāh – Das Gebet im Islam</title>
<link rel="stylesheet" href="https://fonts.googleapis.com/css2?family=EB+Garamond:ital,wght@0,400;0,500;0,600;1,400&display=swap">
<style>
  :root {
    --page: #ffffff;
    --navy-deep: #0b1526;
    --navy: #13254a;
    --navy-glow: #1d3566;
    --gold-dark: #c79a4c;
    --gold: #dcb46b;
    --gold-light: #f3d08d;
    --ink: #111a2a;
    --white: #ffffff;
  }
  * { margin: 0; padding: 0; box-sizing: border-box; }
  html, body {
    width: 1200px;
    height: 1200px;
    overflow: hidden;
    background: var(--page);
  }
  .canvas {
    position: relative;
    width: 1200px;
    height: 1200px;
  }
  .book-cover {
    position: absolute;
    left: 242px;
    top: 61px;
    width: 724px;
    height: 1086px;
    overflow: hidden;
    font-family: "EB Garamond", Georgia, serif;
  }
  .cover-texture {
    position: absolute;
    inset: 0;
    background:
      radial-gradient(ellipse 60% 45% at 52% 50%, var(--navy-glow) 0%, var(--navy) 55%, var(--navy-deep) 100%);
  }
  .title {
    position: absolute;
    left: 0;
    right: 0;
    top: 86px;
    text-align: center;
    font-weight: 600;
    font-size: 150px;
    line-height: 1;
    letter-spacing: 4px;
    background: linear-gradient(180deg, var(--gold-dark) 0%, var(--gold-light) 70%, var(--gold) 100%);
    -webkit-background-clip: text;
    background-clip: text;
    color: transparent;
  }
  .subtitle {
    position: absolute;
    left: 0;
    right: 0;
    top: 276px;
    text-align: center;
    color: var(--white);
    font-size: 63px;
    font-weight: 400;
    line-height: 1;
    letter-spacing: 1px;
  }
  .calligraphy {
    position: absolute;
    left: 188px;
    top: 400px;
    width: 352px;
    height: 284px;
    border-radius: 40%;
    background: radial-gradient(ellipse at 50% 50%, rgba(243, 208, 141, 0.55) 0%, rgba(220, 180, 107, 0.25) 55%, rgba(220, 180, 107, 0) 78%);
  }
  .tagline {
    position: absolute;
    left: 0;
    right: 0;
    top: 834px;
    text-align: center;
    color: var(--white);
    font-style: italic;
    font-size: 60px;
    line-height: 1;
  }
  .author-band {
    position: absolute;
    left: 0;
    right: 0;
    bottom: 0;
    height: 93px;
    background: linear-gradient(180deg, var(--gold-dark) 0%, var(--gold-light) 45%, var(--gold-light) 60%, var(--gold-dark) 100%);
    display: flex;
    align-items: center;
    justify-content: center;
  }
  .author-name {
    color: var(--ink);
    font-size: 48px;
    font-weight: 400;
    letter-spacing: 6px;
    line-height: 1;
    padding-top: 4px;
  }
</style>
</head>
<body>
  <div class="canvas">
    <section class="book-cover">
      <div class="cover-texture" role="img" aria-label="Dunkelblaue, fein rissige Strukturfläche als Hintergrund"></div>
      <h1 class="title">ṢALĀH</h1>
      <p class="subtitle">Das Gebet im Islam</p>
      <div class="calligraphy" role="img" aria-label="Goldene arabische Kalligrafie des Wortes Ṣalāh (صلاة)"></div>
      <p class="tagline">Ein Weg zur Nähe mit Allah</p>
      <div class="author-band">
        <span class="author-name">AURHOR NAME</span>
      </div>
    </section>
  </div>
</body>
</html>
```